Healthy Meal Delivery Website Needs to be updated, current, fresh and modern

Hi there,

The current website i have is super old and outdated.

I would like a beautiful modern site that has all the same content as the previous except with a a new, modern and trustworthy feel.

The current website is https://velmorplatekitchen.com/

Target Market(s)

Health Conscious Young Professionals

Industry/Entity Type

Food Service

Font styles to use
Sans Serif

Requirements
Must have
• Modern Trustworthy feel
Should not have
• Anything out dated or cheesy or scammy

```html
<!DOCTYPE html>
<html lang="en">
<head>
<meta charset="utf-8">
<title>Velmor Plate Kitchen – Diet Meal Delivery</title>
<link href="https://fonts.googleapis.com/css2?family=Roboto:wght@400;500;700&family=Tinos:wght@400;700&display=swap" rel="stylesheet">
<style>
:root{
  --blue:#1ba3dc;
  --blue-dark:#1688bd;
  --yellow:#f2e52a;
  --ink:#222;
  --muted:#555;
  --black:#0d0d0d;
  --grey-bg:#f1f1f1;
  --accent:#3b2360;
  --line:#dedede;
  --white:#fff;
}
*{box-sizing:border-box;margin:0;padding:0}
html,body{width:1200px;height:4128px;overflow:hidden}
body{font-family:"Roboto",Arial,sans-serif;color:var(--ink);background:var(--white);position:relative}
.serif{font-family:"Tinos","Times New Roman",serif}
.topbar{height:36px;background:var(--black);color:var(--white);font-size:15px;display:flex;justify-content:flex-end;align-items:center;gap:26px;padding-right:56px}
.topbar span{display:flex;align-items:center;gap:7px}
.topbar .phone{font-size:20px;font-weight:500}
.header{height:64px;display:flex;align-items:center;justify-content:space-between;padding:0 56px 0 104px}
.brand{display:flex;align-items:center;gap:12px;font-size:22px;font-weight:700;color:var(--blue)}
.brand .dot{width:30px;height:30px;border-radius:50%;background:var(--yellow)}
.nav{display:flex;gap:34px;font-size:15px;color:#333}
.nav a{text-decoration:none;color:inherit;padding-bottom:6px}
.nav a.active{color:var(--blue);border-bottom:3px solid var(--blue)}
.hero{position:relative;height:516px;background:linear-gradient(100deg,#d9d2c6 0%,#e9ece6 35%,#cfc5ba 65%,#b9aba0 100%)}
.hero .arrow{position:absolute;top:212px;width:30px;height:30px;background:rgba(0,0,0,.7);display:flex;align-items:center;justify-content:center}
.hero-caption{position:absolute;left:0;right:0;bottom:0;height:80px;background:rgba(40,40,40,.72);color:var(--white);font-size:25px;text-align:center;line-height:36px;padding-top:5px}
.btn{display:inline-block;background:var(--yellow);color:var(--blue-dark);font-family:"Tinos","Times New Roman",serif;font-weight:700;font-size:19px;border-radius:6px;padding:12px 26px;box-shadow:0 2px 0 #c9bc10}
h2{font-family:"Tinos","Times New Roman",serif;font-weight:700;font-size:28px;text-align:center}
.rule{width:56px;height:3px;background:var(--blue);margin:14px auto 0}
.intro{height:587px;text-align:center;padding-top:66px}
.intro p{font-family:"Tinos",serif;font-size:17px;line-height:28px;margin-top:22px;color:#333}
.features{display:flex;justify-content:center;gap:48px;margin-top:32px}
.feature{width:232px}
.feature .icon{width:116px;height:116px;border-radius:50%;border:4px solid #ddd;margin:0 auto;display:flex;align-items:center;justify-content:center}
.feature h3{font-size:14px;font-weight:700;margin-top:20px}
.feature p{font-family:"Roboto",sans-serif;font-size:12.5px;line-height:18px;margin-top:6px;color:#444}
.intro .btn{margin-top:40px;font-size:18px}
.what{height:352px;background:var(--blue);color:var(--white);text-align:center;padding-top:50px}
.what h2{font-size:36px;font-weight:400}
.what .rule{background:var(--white)}
.what p{font-family:"Tinos",serif;font-size:18px;line-height:40px;margin-top:22px}
.what .btn{margin-top:22px}
.diet{height:735px;position:relative;text-align:center;padding-top:56px}
.diet h2{font-size:36px;font-weight:400}
.diet .sub{font-family:"Tinos",serif;font-size:17px;margin-top:20px}
.diet-photo{position:absolute;left:88px;top:194px;width:380px;height:474px;background:linear-gradient(160deg,#f3f1ec 0%,#e6d8c4 55%,#cbb79a 100%)}
.accordion{position:absolute;left:534px;top:222px;width:556px;text-align:left}
.acc-open{background:var(--blue);color:var(--white);padding:16px 18px 18px;height:115px;border-bottom:4px solid var(--blue-dark)}
.acc-open .row,.acc-item{display:flex;justify-content:space-between;align-items:center;font-family:"Tinos",serif;font-size:15px}
.acc-open p{font-family:"Tinos",serif;font-size:15px;line-height:24px;margin-top:12px}
.acc-item{background:#eee;height:41px;padding:0 18px;margin-top:18px;color:#333}
.acc-item i,.acc-open i{width:18px;height:18px;border-radius:50%;background:var(--accent);color:#fff;font-style:normal;font-size:15px;line-height:18px;text-align:center;font-family:Arial,sans-serif}
.acc-open i{background:var(--white);color:var(--blue)}
.diet .btn{position:absolute;left:538px;top:596px}
.testimonials{height:426px;background:linear-gradient(180deg,#3a2c24 0%,#5a4232 50%,#2e231c 100%);color:var(--white);text-align:center;padding-top:98px}
.testimonials h2{font-size:32px;font-weight:400}
.testimonials blockquote{font-family:"Tinos",serif;font-style:italic;font-size:17px;line-height:30px;width:920px;margin:30px auto 0;color:#eee}
.testimonials cite{display:block;font-style:normal;font-family:"Tinos",serif;font-size:17px;margin-top:20px;color:#ccc}
.dots{display:flex;justify-content:center;gap:8px;margin-top:16px}
.dots b{width:9px;height:9px;border-radius:50%;background:#999}
.dots b:first-child{background:#e39a2c}
.menu{height:688px;text-align:center;padding-top:68px}
.menu h2{font-size:36px;font-weight:400}
.menu p{font-family:"Tinos",serif;font-size:17px;line-height:28px;margin-top:22px}
.cards{display:flex;justify-content:center;gap:26px;margin-top:36px}
.card{width:232px;height:283px;background:var(--white);box-shadow:0 3px 10px rgba(0,0,0,.18);position:relative}
.card .photo{height:173px}
.card h4{font-family:"Tinos",serif;font-weight:400;font-size:17px;margin-top:22px}
.card h4.on{color:var(--blue)}
.card small{display:block;font-size:12.5px;line-height:17px;margin-top:8px;padding:0 18px;color:#444}
.card .tab{position:absolute;right:12px;bottom:-4px;width:40px;height:22px;border-radius:20px 20px 0 0;background:#222;display:flex;align-items:center;justify-content:center}
.card .tab.on{background:var(--blue)}
.card .bar{position:absolute;left:0;bottom:0;height:4px;width:100%;background:var(--blue)}
.menu .btn{margin-top:48px}
.natural{height:353px;background:var(--grey-bg);text-align:center;padding-top:70px}
.natural h2{font-size:27px}
.natural p{font-family:"Tinos",serif;font-size:17px;line-height:28px;margin-top:22px;width:940px;margin-left:auto;margin-right:auto}
.natural .actions{display:flex;justify-content:center;gap:26px;margin-top:50px}
.natural .btn{border:4px solid #f8f29a;padding:8px 22px;font-size:17px}
.footer{height:324px;background:var(--black);color:#ddd;display:flex;padding:46px 0 0 110px;gap:0}
.footer h5{font-size:17px;font-weight:400;color:#eee;margin-bottom:18px}
.col-links{width:184px}
.col-links li{list-style:none;font-size:14px;line-height:32px;color:#ccc}
.col-links li::before{content:"›";margin-right:10px;color:#888}
.col-contact{width:306px;border-left:1px solid #333;padding-left:20px}
.col-contact .item{display:flex;gap:12px;font-size:14px;line-height:20px;margin-bottom:14px}
.col-contact .ic{width:26px;height:26px;border-radius:50%;background:var(--blue);flex:none}
.col-form{width:290px;border-left:1px solid #333;padding-left:20px}
.col-form .field{background:var(--white);color:#333;font-size:13px;height:34px;padding:9px 10px;margin-bottom:8px;width:236px}
.col-form .field.msg{height:72px}
.col-form .submit{display:inline-block;background:var(--blue);color:#fff;font-size:17px;padding:6px 18px;margin-top:4px}
.col-social{border-left:1px solid #333;padding-left:20px}
.social{display:flex;gap:8px}
.social b{width:34px;height:34px;border-radius:50%;background:var(--blue)}
.col-social .brand{margin-top:16px;font-size:17px}
.col-social .brand .dot{width:22px;height:22px}
.copyright{height:47px;background:var(--blue);color:var(--white);font-size:14px;text-align:center;line-height:47px}
</style>
</head>
<body>
<div class="topbar">
  <span>✉ sales@velmorplate.com</span>
  <span class="phone">☏ 416.555.0192</span>
  <span>⇥ Login</span>
  <span>⇥ Signup</span>
</div>
<header class="header">
  <div class="brand"><span class="dot"></span>Velmor Plate Kitchen</div>
  <nav class="nav">
    <a class="active">Home</a><a>Velmor Meal Plans</a><a>Menu</a><a>Pricing</a><a>About</a><a>Press</a><a>Contact Us</a>
  </nav>
</header>

<section class="hero" role="img" aria-label="Fresh salad wraps with dipping sauce beside a slim woman holding a bathroom scale">
  <span class="arrow" style="left:6px"><svg width="12" height="12"><path d="M8 1 3 6l5 5" stroke="#fff" stroke-width="2" fill="none"/></svg></span>
  <span class="arrow" style="right:6px"><svg width="12" height="12"><path d="M4 1l5 5-5 5" stroke="#fff" stroke-width="2" fill="none"/></svg></span>
  <div class="hero-caption">Toronto based diet delivery company that has helped thousands of Canadians slim down and<br>achieve their desired weight loss goals</div>
</section>

<section class="intro">
  <h2>The Velmor Plan Delivers Diet Meals To Your Door In Toronto, Gta And Montreal</h2>
  <p>Our fresh and delicious diet meals and snacks are made with only the best natural ingredients that nourish your body.<br>Why not let us prepare your meals while you lose the weight?</p>
  <div class="features">
    <div class="feature">
      <div class="icon" style="background:var(--yellow)"><svg width="50" height="46" viewBox="0 0 50 46"><path d="M25 44 5 24A12 12 0 0 1 25 8a12 12 0 0 1 20 16Z" fill="var(--blue)"/><path d="M25 18v14M18 25h14" stroke="#fff" stroke-width="4"/></svg></div>
      <h3>HEALTHY</h3>
      <p>The Velmor Plan is a great way to ensure you are eating all the nutrients you need, and nothing your body doesn't need.</p>
    </div>
    <div class="feature">
      <div class="icon" style="background:#2a2a2a"><svg width="46" height="46" viewBox="0 0 46 46" fill="none" stroke="#fff" stroke-width="3"><rect x="6" y="6" width="20" height="20" rx="3"/><rect x="20" y="20" width="20" height="20" rx="3"/></svg></div>
      <h3>CHOICE</h3>
      <p>You can choose your own meals from over 100 tasty entrees, desserts &amp; snack foods. You can choose your meals online.</p>
    </div>
    <div class="feature">
      <div class="icon" style="background:#2a2a2a"><svg width="52" height="40" viewBox="0 0 52 40"><path d="M4 18h44a22 18 0 0 1-44 0Z" fill="#fff"/><circle cx="18" cy="12" r="5" fill="#fff"/><circle cx="30" cy="9" r="6" fill="#fff"/></svg></div>
      <h3>FRESH</h3>
      <p>All of our meals are real food, freshly prepared by our in-house expert chefs.</p>
    </div>
    <div class="feature">
      <div class="icon" style="background:#2a2a2a"><svg width="54" height="40" viewBox="0 0 54 40" fill="#fff"><rect x="2" y="6" width="32" height="22" rx="2"/><path d="M36 12h9l7 8v8H36Z"/><circle cx="12" cy="32" r="5"/><circle cx="44" cy="32" r="5"/></svg></div>
      <h3>CUSTOMIZED</h3>
      <p>Your meals will be delivered fresh to your door, customized for your unique body type and level of activity.</p>
    </div>
  </div>
  <span class="btn">Get Started</span>
</section>

<section class="what">
  <h2>What is Velmor?</h2>
  <div class="rule"></div>
  <p>Velmor is the Toronto &amp; Montreal Diet Delivery program based on the Velmor Plan™, healthy carbs and the right fats.<br>We provide you with 3 fresh meals, 2 snacks and a dessert delivered to your door before 6am.<br>Try our Velmor Plan™ delivery plan and start Velmor weight loss now!</p>
  <span class="btn">Try our Velmor Plan™ Today</span>
</section>

<section class="diet">
  <h2>The Velmor Plan</h2>
  <div class="rule"></div>
  <p class="sub">Real foods designed by nature prepared by Velmor.</p>
  <div class="diet-photo" role="img" aria-label="Smiling woman in a yellow top measuring her waist beside a bowl of salad"></div>
  <div class="accordion">
    <div class="acc-open">
      <div class="row">WHAT YOU GET <i>−</i></div>
      <p>Velmor Plan Delivery provides you with 3 fresh daily meals and 3 snacks delivered to your doorstep before 6am.</p>
    </div>
    <div class="acc-item">SELECTION <i>+</i></div>
    <div class="acc-item">LUXURY <i>+</i></div>
    <div class="acc-item">WHAT IS PHASE 1? <i>+</i></div>
    <div class="acc-item">WHAT IS PHASE 2? <i>+</i></div>
  </div>
  <span class="btn">Try our Velmor Plan™ Today</span>
</section>

<section class="testimonials" role="img" aria-label="Dimmed background of a plated pasta dish">
  <h2>Clients Testimonials</h2>
  <blockquote>" Lorem ipsum dolor sit amet, consectetuer adipiscing elit, sed diam nonummy nibh euismod tincidunt ut laoreet dolore magna aliquam erat volutpat. Ut wisi enim ad minim veniam, quis nostrud exercitation ullamcorper suscipit lobortis nisl ut aliquip ex ea commodo consequat "</blockquote>
  <cite>Mr. Lorem Ipsum</cite>
  <div class="dots"><b></b><b></b><b></b><b></b></div>
</section>

<section class="menu">
  <h2>Select From Over 100 Menu Items</h2>
  <div class="rule"></div>
  <p>You can choose your own meals from over 100 tasty entrees, desserts and snack foods.<br>You can choose your meals online, or we can select your meals for you.</p>
  <div class="cards">
    <div class="card"><div class="photo" role="img" aria-label="Cobb lettuce wraps" style="background:linear-gradient(135deg,#dfe9c8,#9cc06a)"></div><h4 class="on">Snacks</h4><small>Cobb Lettuce Wrap</small><span class="tab on"><svg width="12" height="8"><path d="M1 7 6 2l5 5" stroke="#fff" stroke-width="2" fill="none"/></svg></span><span class="bar"></span></div>
    <div class="card"><div class="photo" role="img" aria-label="Scrambled eggs with dill and smoked salmon" style="background:linear-gradient(135deg,#f6d34a,#e8833a)"></div><h4>Breakfast</h4><small>Scrambled Eggs with Dill &amp; Smoked Salmon</small><span class="tab"><svg width="12" height="8"><path d="M1 7 6 2l5 5" stroke="#fff" stroke-width="2" fill="none"/></svg></span></div>
    <div class="card"><div class="photo" role="img" aria-label="Roasted beet, walnut and goat cheese salad" style="background:linear-gradient(135deg,#8a3a44,#c9b79a)"></div><h4>Lunch</h4><small>Roasted Beet Walnut And Goat Cheese Salad</small><span class="tab"><svg width="12" height="8"><path d="M1 7 6 2l5 5" stroke="#fff" stroke-width="2" fill="none"/></svg></span></div>
    <div class="card"><div class="photo" role="img" aria-label="Grilled salmon steak with parsnip over collard greens" style="background:linear-gradient(135deg,#e7a06a,#4a6a34)"></div><h4>Dorem Hollo</h4><small>Grilled Salmon Steak With Baked Parsnip Over Collard Greens</small><span class="tab"><svg width="12" height="8"><path d="M1 7 6 2l5 5" stroke="#fff" stroke-width="2" fill="none"/></svg></span></div>
  </div>
  <span class="btn">Try our Velmor Plan™ Today</span>
</section>

<section class="natural">
  <h2>The Velmor Plan Is Based On Real Foods Made With Fresh And Natural Ingredients.</h2>
  <p>It's about eating the foods you love and emphasizing the ones that nourish your body; generous portions of fresh fruit, vegetables, meat, fish, nuts and seeds, with smaller servings of grains and dairy.</p>
  <div class="actions">
    <span class="btn">⇥ Customer Login</span>
    <span class="btn">⇥ SignUp Now</span>
  </div>
</section>

<footer class="footer">
  <div class="col-links">
    <h5>Quick Links</h5>
    <ul><li>Home</li><li>Velmor Meal Plans</li><li>Menu</li><li>Pricing</li><li>About</li><li>Press</li></ul>
  </div>
  <div class="col-contact">
    <h5>Contact Details</h5>
    <div class="item"><span class="ic"></span><span>Toronto<br>416-555-0192</span></div>
    <div class="item"><span class="ic"></span><span>Email<br>sales@velmorplate.com</span></div>
  </div>
  <div class="col-form">
    <h5>Quick Inquiry</h5>
    <div class="field">Name</div>
    <div class="field">Email</div>
    <div class="field msg">Message</div>
    <span class="submit">Submit →</span>
  </div>
  <div class="col-social">
    <h5>Follow Us</h5>
    <div class="social"><b></b><b></b><b></b><b></b></div>
    <div class="brand"><span class="dot"></span>Velmor Plate Kitchen</div>
  </div>
</footer>
<div class="copyright">Copyright © 2018 VelmorPlateKitchen. All Rights Reserved.</div>
</body>
</html>
```